Hairdressing Salon called; Tressel Studio. Style Is Us

Tressel Studio
We Love Hair
418 Wexbury Lane Hollin Park
4839172
Business card not to fussy.
I would like it to be a Black background with White and/or Grey lettering.

I really like the business card attached, so if the front looked like this I would be really happy, but would also like my address and phone number on the front.

On the back I would like two options of
1: reward card; buy any Haircare product over $20 on any visit and on the tenth product receive a complimentry Treatment and
2: appointment times and date

Business

Tressel Studio
We Love Hair
4839172
418 Wexbury Lane, Hollin Park
This must all be included on the front of the card

Serif
Decorative
Script

1b1b1b
757575
ffffff

Must have
• My phone number and address
Should not have
• Pictures on the front

```html
<!DOCTYPE html>
<html lang="en">
<head>
<meta charset="utf-8">
<title>Tressel Studio – Business Card</title>
<link rel="stylesheet" href="https://fonts.googleapis.com/css2?family=Tinos:wght@400;700&display=swap">
<style>
  :root {
    --page: #ffffff;
    --card: #231f1e;
    --ink: #ffffff;
    --ink-soft: #e6e3e1;
    --grey: #757575;
    --damask: #3a3533;
    --ornament: #d9d6d3;
  }
  * { box-sizing: border-box; margin: 0; padding: 0; }
  html, body {
    width: 900px; height: 1200px; overflow: hidden;
    background: var(--page);
    font-family: "Tinos", "Times New Roman", serif;
  }
  .sheet {
    width: 900px; height: 1200px;
    display: flex; flex-direction: column; align-items: center; justify-content: center;
    gap: 56px;
  }
  .card {
    position: relative; width: 640px; height: 363px;
    background: var(--card); color: var(--ink); overflow: hidden;
  }
  .card-frame { position: absolute; inset: 0; }
  .damask {
    position: absolute; left: 200px; top: 40px; width: 240px; height: 280px;
    background: radial-gradient(ellipse at center, var(--damask) 0%, rgba(58,53,51,0.55) 45%, rgba(35,31,30,0) 72%);
  }
  .flourish {
    position: absolute; left: 187px; top: 42px; width: 266px; height: 44px;
    background: linear-gradient(90deg, rgba(217,214,211,0) 0%, var(--ornament) 20%, var(--ornament) 80%, rgba(217,214,211,0) 100%);
    opacity: 0.75; border-radius: 22px;
  }
  .front-details {
    position: absolute; left: 0; right: 0; top: 120px; text-align: center;
  }
  .salon-name { font-size: 34px; font-weight: 400; letter-spacing: 0.3px; }
  .address, .phone-short { font-size: 17px; color: var(--ink-soft); line-height: 24px; }
  .address { margin-top: 14px; }
  .phone { font-size: 17px; color: var(--ink-soft); margin-top: 18px; }
  .tagline {
    position: absolute; left: 0; right: 0; top: 282px; text-align: center;
    font-size: 30px; letter-spacing: 0.5px;
  }
  .offers {
    position: absolute; left: 74px; top: 132px; font-size: 17px; line-height: 22px; color: var(--ink-soft);
  }
  .offer-title { font-weight: 700; color: var(--ink); }
  .offer-body { padding-left: 20px; }
  .offer + .offer { margin-top: 16px; }
</style>
</head>
<body>
<main class="sheet">

  <section class="card card-front" aria-label="Business card front">
    <div class="damask" role="img" aria-label="Faint damask pattern behind the text"></div>
    <svg class="card-frame" viewBox="0 0 640 363" aria-hidden="true">
      <g fill="none" stroke="#ffffff" stroke-width="2">
        <rect x="24" y="24" width="592" height="315"/>
        <line x1="100" y1="96" x2="540" y2="96"/>
        <line x1="100" y1="303" x2="200" y2="303"/>
        <line x1="440" y1="303" x2="540" y2="303"/>
      </g>
      <g fill="#ffffff">
        <circle cx="14" cy="14" r="5"/><circle cx="626" cy="14" r="5"/>
        <circle cx="14" cy="349" r="5"/><circle cx="626" cy="349" r="5"/>
        <circle cx="100" cy="96" r="4"/><circle cx="540" cy="96" r="4"/>
        <circle cx="100" cy="303" r="4"/><circle cx="540" cy="303" r="4"/>
      </g>
    </svg>
    <div class="flourish" role="img" aria-label="Decorative scrollwork flourish"></div>
    <div class="front-details">
      <h1 class="salon-name">Tressel Studio</h1>
      <p class="address">418 Wexbury Lane Hollin Park</p>
      <p class="phone-short">4839172</p>
      <p class="phone">Phone: +987 555 0142 3861</p>
    </div>
    <p class="tagline">We Love Hair</p>
  </section>

  <section class="card card-back" aria-label="Business card back">
    <div class="damask" role="img" aria-label="Faint damask pattern behind the text"></div>
    <svg class="card-frame" viewBox="0 0 640 363" aria-hidden="true">
      <g fill="none" stroke="#ffffff" stroke-width="2">
        <rect x="24" y="24" width="592" height="315"/>
        <line x1="100" y1="96" x2="540" y2="96"/>
        <line x1="100" y1="303" x2="200" y2="303"/>
        <line x1="440" y1="303" x2="540" y2="303"/>
      </g>
      <g fill="#ffffff">
        <circle cx="14" cy="14" r="5"/><circle cx="626" cy="14" r="5"/>
        <circle cx="14" cy="349" r="5"/><circle cx="626" cy="349" r="5"/>
        <circle cx="100" cy="96" r="4"/><circle cx="540" cy="96" r="4"/>
        <circle cx="100" cy="303" r="4"/><circle cx="540" cy="303" r="4"/>
      </g>
    </svg>
    <div class="flourish" role="img" aria-label="Decorative scrollwork flourish"></div>
    <div class="offers">
      <div class="offer">
        <p class="offer-title">1. Reward card:</p>
        <p class="offer-body">buy any Haircare product over $20 on any visit<br>and on the tenth product receive a complimentry Treatment</p>
      </div>
      <div class="offer">
        <p class="offer-title">2. Appointment times and date</p>
      </div>
    </div>
    <p class="tagline">We Love Hair</p>
  </section>

</main>
</body>
</html>
```